Global Consulting firm needs a Business Card Design (Contest)

We need a business card design for a company with global reach called 'Hollowbrook Group'. Hollowbrook Group is a Trusted Procurement Advisor that consults for Pinnacle 400 and Meridel 900 companies to find cost reductions in their spending. We would like to see designs that communicate fiduciary trust and sense of partnership. The Front should have our logo w/ 'trusted procurement advisor', Employee name and title, company address, email, phone and fax (logo attached "Hollowbrook group final"). The color scheme and basic concept should be consistent with our presentation front page (attached "HBG presentation cover page"). The Back should have our website (www.hwbrookllc.com) and an array of our areas of expertise: office supplies, lab supplies, wireless telecom, MRO and IT (see "lab supplies" file for example).

```html
<!DOCTYPE html>
<html lang="en">
<head>
<meta charset="utf-8">
<title>Hollowbrook Group – Business Card</title>
<link rel="stylesheet" href="https://fonts.googleapis.com/css2?family=Source+Sans+3:wght@400;600&family=Gentium+Book+Plus:ital,wght@0,400;1,400&display=swap">
<style>
  :root {
    --backdrop: #5b3f2c;
    --card: #ffffff;
    --gold: #c9a02a;
    --gold-dark: #b08a1e;
    --ink: #1d1d1d;
    --map-tone: #f4ecdc;
    --band: #141414;
    --tile-line: #c9a02a;
  }
  * { box-sizing: border-box; margin: 0; padding: 0; }
  html, body { width: 1200px; height: 1000px; overflow: hidden; }
  body {
    background: var(--backdrop);
    position: relative;
    font-family: "Source Sans 3", Arial, sans-serif;
    color: var(--ink);
  }
  .card {
    position: absolute;
    left: 265px;
    width: 665px;
    height: 397px;
    background: var(--card);
    border-radius: 22px;
    overflow: hidden;
    box-shadow: 0 4px 14px rgba(0,0,0,.35);
  }
  .card--front { top: 73px; }
  .card--back { top: 532px; }

  /* front */
  .world-map {
    position: absolute;
    left: 40px; top: 8px;
    width: 605px; height: 290px;
    border-radius: 60px 90px 70px 40px;
    background: radial-gradient(ellipse at 50% 45%, var(--map-tone) 0%, rgba(244,236,220,.55) 60%, rgba(255,255,255,0) 100%);
  }
  .person { position: absolute; left: 0; width: 665px; text-align: center; }
  .person__name {
    top: 74px; left: 0; font-size: 33px; font-weight: 600; color: var(--gold);
    padding-left: 0; transform: translateX(0);
  }
  .person__title { top: 106px; font-size: 26px; color: var(--ink); }
  .person__name, .person__title { width: 665px; margin-left: 0; }
  .person__name { text-indent: 0; }
  .person { left: 0; }
  .person__name, .person__title { left: 0; }
  .person__name { width: 666px; }

  .brand-name {
    font-family: "Gentium Book Plus", Georgia, serif;
    color: var(--ink);
    white-space: nowrap;
  }
  .front-brand { position: absolute; right: 32px; top: 200px; text-align: center; }
  .front-brand .brand-name { font-size: 27px; line-height: 1; }
  .tagline {
    font-family: "Gentium Book Plus", Georgia, serif;
    font-style: italic;
    color: var(--ink);
  }
  .front-brand .tagline { font-size: 14.5px; margin-top: 4px; }

  .rule {
    position: absolute; left: 32px; top: 274px;
    width: 601px; height: 2px; background: var(--gold);
  }
  .contacts { position: absolute; left: 33px; top: 287px; list-style: none; }
  .contacts li {
    display: flex; align-items: center; gap: 7px;
    height: 27px; font-size: 16.5px;
  }
  .contacts svg { width: 21px; height: 21px; flex: none; }
  .address {
    position: absolute; right: 32px; top: 288px;
    text-align: right; font-size: 16.5px; line-height: 22px; font-style: normal;
  }

  /* back */
  .back-brand {
    position: absolute; top: 68px; left: 0; width: 665px;
    display: flex; justify-content: center; align-items: center; gap: 14px;
  }
  .brand-mark { width: 54px; height: 54px; border-radius: 50%; background: var(--gold); flex: none; }
  .back-brand .brand-name { font-size: 41px; line-height: 1; }
  .back-tagline {
    position: absolute; top: 124px; left: 218px; width: 304px; text-align: center;
    font-size: 23px;
  }
  .web-band {
    position: absolute; top: 186px; left: 0; width: 665px; height: 26px;
    background: var(--band); color: var(--gold);
    text-align: center; font-size: 16px; font-weight: 600;
    letter-spacing: 3px; line-height: 26px;
  }
  .expertise {
    position: absolute; top: 255px; left: 46px;
    display: flex; gap: 14px; list-style: none;
  }
  .expertise__item {
    position: relative; width: 104px; height: 74px;
    border: 1.5px solid var(--tile-line); background: #fff;
  }
  .expertise__photo { position: absolute; left: 6px; right: 6px; top: 12px; bottom: 4px; }
  .expertise__label {
    position: absolute; left: -1px; top: -1px;
    height: 13px; padding: 0 8px;
    background: var(--gold); color: #111;
    font-size: 9.5px; line-height: 13px;
    border-radius: 0 6px 0 0; white-space: nowrap;
  }
  .photo--office { background: linear-gradient(135deg, #d6d0c8, #8a7f76 60%, #c94a3a); }
  .photo--lab { background: linear-gradient(135deg, #e9eef2, #9fc3d4 60%, #6bbf5a); }
  .photo--telecom { background: linear-gradient(135deg, #ffffff, #3a8fd6 55%, #2b2b2b); }
  .photo--mro { background: linear-gradient(135deg, #9aa5ae, #4f5a63 60%, #c5a88a); }
  .photo--it { background: linear-gradient(135deg, #3a8ecf, #1e4f86 60%, #e8eef4); }
</style>
</head>
<body>

<section class="card card--front" aria-label="Card front">
  <div class="world-map" role="img" aria-label="Faint world map in the background"></div>
  <p class="person person__name">Daniel Whitcombe</p>
  <p class="person person__title">Manager</p>

  <div class="front-brand">
    <p class="brand-name">Hollowbrook Group</p>
    <p class="tagline">Trusted Procurement Advisor</p>
  </div>

  <div class="rule"></div>

  <ul class="contacts">
    <li>
      <svg viewBox="0 0 22 22" aria-hidden="true"><circle cx="11" cy="11" r="10" fill="none" stroke="#c9a02a" stroke-width="1.6"/><path d="M6 9c0-1.5 2.2-2.5 5-2.5s5 1 5 2.5l-1.8.6-.6-1.3c-1.7-.5-3.5-.5-5.2 0l-.6 1.3zM7.5 11h7l.8 4h-8.6z" fill="#c9a02a"/></svg>
      <span>555 - 318 - 4420</span>
    </li>
    <li>
      <svg viewBox="0 0 22 22" aria-hidden="true"><circle cx="11" cy="11" r="10" fill="none" stroke="#c9a02a" stroke-width="1.6"/><rect x="7.5" y="5.5" width="7" height="4" fill="#c9a02a"/><rect x="5.5" y="9.5" width="11" height="5" rx="1" fill="#c9a02a"/><rect x="7.5" y="13" width="7" height="3.5" fill="#fff" stroke="#c9a02a"/></svg>
      <span>555 - 672 - 0915</span>
    </li>
    <li>
      <svg viewBox="0 0 22 22" aria-hidden="true"><circle cx="11" cy="11" r="10" fill="none" stroke="#c9a02a" stroke-width="1.6"/><rect x="5.5" y="7.5" width="11" height="7.5" fill="#c9a02a"/><path d="M5.5 7.5l5.5 4.5 5.5-4.5" fill="none" stroke="#fff" stroke-width="1"/></svg>
      <span>info@hwbrookllc.com</span>
    </li>
  </ul>

  <address class="address">
    4100 Larchmont Avenue, Suite 210,<br>
    Glen Harbor, NJ 07990
  </address>
</section>

<section class="card card--back" aria-label="Card back">
  <div class="back-brand">
    <span class="brand-mark" aria-hidden="true"></span>
    <p class="brand-name">Hollowbrook Group</p>
  </div>
  <p class="tagline back-tagline">Trusted Procurement Advisor</p>

  <div class="web-band">www.hwbrookllc.com</div>

  <ul class="expertise">
    <li class="expertise__item">
      <span class="expertise__label">Office Supplies</span>
      <div class="expertise__photo photo--office" role="img" aria-label="Photo of assorted office supplies"></div>
    </li>
    <li class="expertise__item">
      <span class="expertise__label">Lap Supplies</span>
      <div class="expertise__photo photo--lab" role="img" aria-label="Photo of laboratory glassware and microscope"></div>
    </li>
    <li class="expertise__item">
      <span class="expertise__label">Wireless Telecom</span>
      <div class="expertise__photo photo--telecom" role="img" aria-label="Illustration of a smartphone beside a globe"></div>
    </li>
    <li class="expertise__item">
      <span class="expertise__label">MRO</span>
      <div class="expertise__photo photo--mro" role="img" aria-label="Photo of a technician servicing equipment"></div>
    </li>
    <li class="expertise__item">
      <span class="expertise__label">IT</span>
      <div class="expertise__photo photo--it" role="img" aria-label="Photo of network cables plugged into a switch"></div>
    </li>
  </ul>
</section>

</body>
</html>
```